Biz Card for Harrowfield Property Partners - HWPP

Harrowfield Property Partners is a commercial real estate acquisitions firm. We buy commercial property and need to raise capital from investors for each deal we buy. The vibe needs to be: give us your money, we will multiply it.
Our website: www.hrwpp-example.com
Competitors are: https://velmarholdings-example.com/, https://tribanquepartners-example.com/, http://www.ostrellecapital-example.com/
Target Market(s)
High Net Worth Individuals, Bankers, Insurance Companies, Commercial Real Estate Brokers.
Industry/Entity Type
Investment Banking
Contact Information for Business Card
Name, Title, Addess, Cell#, Office#, email, website
Requirements
Must have
- use one of our logos. See website for look and feel: www.hrwpp-example.com
Nice to have
- see website: www.hrwpp-example.com

```html
<!DOCTYPE html>
<html lang="en">
<head>
<meta charset="utf-8">
<title>Harrowfield Property Partners – Business Card</title>
<link rel="stylesheet" href="https://fonts.googleapis.com/css2?family=Lato:wght@300;400&family=Montserrat:wght@500;600&display=swap">
<style>
  :root {
    --navy: #03263d;
    --navy-deep: #02243d;
    --green: #066a50;
    --white: #ffffff;
    --ink: #0d2238;
    --card-edge: #1c1c1c;
  }
  html, body {
    margin: 0;
    width: 1200px;
    height: 1000px;
    overflow: hidden;
    background: var(--white);
  }
  .canvas {
    position: relative;
    width: 1200px;
    height: 1000px;
  }
  .card {
    position: absolute;
    left: 206px;
    width: 786px;
    height: 449px;
    outline: 1px solid var(--card-edge);
    display: block;
  }
  .card--front { top: 37px; }
  .card--back { top: 510px; }
  .brand-name {
    font-family: "Lato", sans-serif;
    font-weight: 400;
    fill: var(--white);
  }
  .web-address {
    font-family: "Montserrat", sans-serif;
    font-weight: 500;
    fill: var(--ink);
    letter-spacing: 1px;
  }
  .contact-text {
    font-family: "Montserrat", sans-serif;
    font-weight: 600;
    fill: var(--white);
  }
  .icon { fill: var(--white); }
  .icon-line { fill: none; stroke: var(--white); stroke-width: 2; }
</style>
</head>
<body>
<main class="canvas">

  <!-- Front of card -->
  <svg class="card card--front" viewBox="0 0 786 449" aria-label="Business card front">
    <defs>
      <linearGradient id="brandGradFront" x1="0" y1="0" x2="786" y2="0" gradientUnits="userSpaceOnUse">
        <stop offset="0" stop-color="var(--navy)"/>
        <stop offset="1" stop-color="var(--green)"/>
      </linearGradient>
    </defs>
    <rect class="card-base" width="786" height="449" fill="var(--white)"/>
    <rect class="top-band" width="786" height="156" fill="url(#brandGradFront)"/>
    <rect class="accent-band" y="156" width="786" height="82" fill="var(--navy-deep)"/>
    <path class="brand-plate" d="M76,150 L711,150 L685,350 Q682,370 660,370 L120,370 Q100,370 98,350 Z" fill="url(#brandGradFront)"/>
    <circle class="brand-dot" cx="391" cy="181" r="53" fill="var(--white)"/>
    <text class="brand-name" x="391" y="283" text-anchor="middle" font-size="36" letter-spacing="5">HARROWFIELD</text>
    <text class="brand-name" x="391" y="310" text-anchor="middle" font-size="15" letter-spacing="4">PROPERTY PARTNERS</text>
    <text class="web-address" x="393" y="414" text-anchor="middle" font-size="21">www.hrwpp-example.com</text>
  </svg>

  <!-- Back of card -->
  <svg class="card card--back" viewBox="0 0 786 449" aria-label="Business card back">
    <defs>
      <linearGradient id="brandGradBack" x1="0" y1="0" x2="786" y2="0" gradientUnits="userSpaceOnUse">
        <stop offset="0" stop-color="var(--navy)"/>
        <stop offset="1" stop-color="var(--green)"/>
      </linearGradient>
      <linearGradient id="rowGrad" x1="380" y1="0" x2="786" y2="0" gradientUnits="userSpaceOnUse">
        <stop offset="0" stop-color="var(--navy)"/>
        <stop offset="1" stop-color="var(--green)"/>
      </linearGradient>
    </defs>
    <rect class="card-base" width="786" height="449" fill="var(--white)"/>
    <rect class="main-field" width="786" height="393" fill="url(#brandGradBack)"/>
    <polygon class="slash-accent" points="683,0 748,0 689,93 624,93" fill="var(--white)"/>
    <rect class="side-tab" x="0" y="165" width="13" height="145" fill="var(--white)"/>

    <!-- Contact panel -->
    <path class="contact-frame" d="M786,164 L406,164 Q388,164 384,181 L340,380 Q337,393 325,393 L786,393 Z" fill="var(--white)"/>
    <path class="contact-row" d="M391,184 Q394,171 408,171 L778,171 L778,240 L377,240 Z" fill="url(#rowGrad)"/>
    <path class="contact-row" d="M376,246 L778,246 L778,316 L362,316 Z" fill="url(#rowGrad)"/>
    <path class="contact-row" d="M361,322 L778,322 L778,393 L347,393 Z" fill="url(#rowGrad)"/>

    <text class="contact-text" x="560" y="215" text-anchor="middle" font-size="19">(305) 555-0142</text>
    <text class="contact-text" x="545" y="290" text-anchor="middle" font-size="18">info@hrwpp-example.com</text>
    <text class="contact-text" x="392" y="351" font-size="19">USA: 480 Marlow Ave, Suite</text>
    <text class="contact-text" x="392" y="375" font-size="19">740 Brookvale Park, FL 33190</text>

    <!-- Phone icon -->
    <g class="icon icon--phone" transform="translate(734,205)">
      <path d="M-15,-7 Q0,-16 15,-7 L15,-2 L9,-2 L9,-6 L-9,-6 L-9,-2 L-15,-2 Z"/>
      <path d="M-9,-1 L9,-1 L13,12 L-13,12 Z"/>
      <circle cx="0" cy="5" r="4" fill="var(--navy)"/>
      <circle cx="0" cy="5" r="2"/>
    </g>
    <!-- Envelope icon -->
    <g class="icon icon--mail" transform="translate(734,280)">
      <rect x="-15" y="-10" width="30" height="21" class="icon-line"/>
      <path d="M-15,-10 L0,3 L15,-10" class="icon-line"/>
      <path d="M-15,11 L-4,0 M15,11 L4,0" class="icon-line"/>
    </g>
    <!-- Location pin icon -->
    <g class="icon icon--pin" transform="translate(734,352)">
      <path d="M0,18 L-10,4 A12,12 0 1,1 10,4 Z"/>
      <circle cx="0" cy="-4" r="4.5" fill="var(--green)"/>
    </g>

    <!-- Brand mark -->
    <circle class="brand-dot" cx="190" cy="202" r="46" fill="var(--white)"/>
    <text class="brand-name" x="188" y="289" text-anchor="middle" font-size="29" letter-spacing="3">HARROWFIELD</text>
    <text class="brand-name" x="188" y="314" text-anchor="middle" font-size="13" letter-spacing="3">PROPERTY PARTNERS</text>

    <text class="web-address" x="395" y="427" text-anchor="middle" font-size="21">www.hrwpp-example.com</text>
  </svg>

</main>
</body>
</html>
```